Lanterne architecture business cards

We are a new company based in New Zealand. We Specialize in High end Luxury Residential Architecture.

Every home is bespoke and is designed to each clients individual requirements and needs.

I like to design buildings that inspire people through light and form while offering a high level of comfort and usability.

Lines of sight, proportion and balance are fundamental to the spaces I create.
Updates

August 5th is current deadline - Today's date is the 13th of August.

Target Market(s)

New Zealanders who want a custom individual home design, typically 30-65 year old males and females

Industry/Entity Type

Architecture

Contact Information for Business Card

Director - Derek Tolson
Contact Number - 0279164073
Email - info@lanternearchitecture-example.co.nz
Webstie - www.lanternearchitecture-example.co.nz
Social Media - @lanternearchitecture

Font styles to use
Sans Serif

Requirements
Must have
• Logo (Both Sides)
Website
Email
Contact Number
Social Media

Nice to have
• Texture
Should not have
• More than 3 colours - typically I would've thought 2 would be good to match the logo.

```html
<!DOCTYPE html>
<html lang="en">
<head>
<meta charset="utf-8">
<title>Lanterne architecture business cards</title>
<link href="https://fonts.googleapis.com/css2?family=Open+Sans:wght@400;700&display=swap" rel="stylesheet">
<style>
  :root {
    --canvas: #e9e7e3;
    --card-light: #ffffff;
    --card-dark: #0e0e0f;
    --ink: #222222;
    --ink-soft: #555555;
    --brand-grey: #5a5a5a;
    --rule: #cfcfcf;
    --white: #ffffff;
  }
  * { margin: 0; padding: 0; box-sizing: border-box; }
  html, body {
    width: 1200px; height: 1024px; overflow: hidden;
    background: var(--canvas);
    font-family: "Open Sans", Arial, sans-serif;
  }
  .sheet {
    width: 1200px; height: 1024px;
    display: flex; flex-direction: column;
    align-items: center; justify-content: center; gap: 56px;
  }
  .card {
    width: 720px; height: 411px;
    position: relative; overflow: hidden;
    box-shadow: 0 10px 28px rgba(0,0,0,0.18);
  }
  .card--front { background: var(--card-light); display: flex; }
  .card--back {
    background: linear-gradient(135deg, #1c1c1e 0%, var(--card-dark) 55%, #050505 100%);
    display: flex; align-items: center; justify-content: center;
  }

  .brand {
    display: flex; align-items: center; gap: 10px;
    font-weight: 400; font-size: 22px; line-height: 1;
    white-space: nowrap;
  }
  .brand__square { width: 14px; height: 14px; background: currentColor; }
  .card--front .brand { color: var(--brand-grey); }
  .card--back .brand { color: var(--white); font-size: 26px; }
  .card--back .brand__square { width: 16px; height: 16px; }

  .front__brand-area {
    width: 330px; display: flex; align-items: center; justify-content: center;
  }
  .front__divider { width: 1px; background: var(--rule); margin: 60px 0; }
  .front__details { flex: 1; padding: 58px 0 0 38px; color: var(--ink); }
  .person__name { font-weight: 700; font-size: 25px; line-height: 1.15; }
  .person__role { font-weight: 700; font-size: 15px; margin-bottom: 30px; }
  .contact { list-style: none; font-size: 14.5px; color: var(--ink-soft); line-height: 1.75; }
  .social { display: flex; align-items: center; gap: 6px; margin-top: 18px; font-size: 14.5px; color: var(--ink-soft); }
  .social__icon { width: 17px; height: 17px; background: var(--ink); border-radius: 2px; }
  .social__handle { margin-left: 8px; }
</style>
</head>
<body>
<main class="sheet">
  <section class="card card--front" aria-label="Business card front">
    <div class="front__brand-area">
      <div class="brand">
        <span class="brand__square" aria-hidden="true"></span>
        <span class="brand__name">Lanterne architecture</span>
      </div>
    </div>
    <div class="front__divider" aria-hidden="true"></div>
    <div class="front__details">
      <h1 class="person__name">Derek Tolson</h1>
      <p class="person__role">Director</p>
      <ul class="contact">
        <li>0279164073</li>
        <li>info@lanternearchitecture-example.co.nz</li>
        <li>www.lanternearchitecture-example.co.nz</li>
      </ul>
      <div class="social">
        <span class="social__icon" aria-hidden="true"></span>
        <span class="social__icon" aria-hidden="true"></span>
        <span class="social__icon" aria-hidden="true"></span>
        <span class="social__handle">@lanternearchitecture</span>
      </div>
    </div>
  </section>

  <section class="card card--back" aria-label="Business card back">
    <div class="brand">
      <span class="brand__square" aria-hidden="true"></span>
      <span class="brand__name">Lanterne architecture</span>
    </div>
  </section>
</main>
</body>
</html>
```